Morvela Aesthetic Doctor

I require an elegant, luxurious looking business card for my aesthetic business. I am a doctor and that will set me aside from competitors. I am planning to provide home and spa based treatments to clients with high expectations. I have attached my logo.

```html
<!DOCTYPE html>
<html lang="en">
<head>
<meta charset="utf-8">
<title>Morvela Aesthetic Doctor – Business Card</title>
<link href="https://fonts.googleapis.com/css2?family=Open+Sans:wght@300;400&display=swap" rel="stylesheet">
<style>
  :root {
    --backdrop: #e6e7e8;
    --card: #ffffff;
    --accent: #00aeef;
    --ink: #333333;
    --mark-grey: #a7a9ac;
  }
  * { margin: 0; padding: 0; box-sizing: border-box; }
  html, body { width: 1169px; height: 1200px; overflow: hidden; }
  body {
    background: var(--backdrop);
    font-family: "Open Sans", Arial, sans-serif;
    font-weight: 300;
    color: var(--ink);
    position: relative;
  }
  .card {
    position: absolute;
    left: 154px;
    width: 860px;
    height: 491px;
    background: var(--card);
  }
  .card--front { top: 93px; }
  .card--back { top: 614px; }

  .front-frame {
    position: absolute;
    left: 29px; top: 29px;
    width: 802px; height: 433px;
    border: 3px solid var(--accent);
  }

  .brand {
    position: absolute;
    display: flex;
    align-items: center;
    color: var(--mark-grey);
    font-weight: 300;
  }
  .brand__circle {
    border: 2px solid var(--mark-grey);
    border-radius: 50%;
    flex: none;
  }
  .brand__name { line-height: 1; letter-spacing: 0.04em; }
  .brand__name span { display: block; }

  .brand--front { left: 260px; top: 126px; }
  .brand--front .brand__circle { width: 118px; height: 118px; margin-right: 22px; }
  .brand--front .brand__word { font-size: 56px; }
  .brand--front .brand__sub { font-size: 23px; margin-top: 10px; letter-spacing: 0.06em; }

  .brand--back { right: 31px; top: 64px; }
  .brand--back .brand__circle { width: 86px; height: 86px; margin-right: 14px; }
  .brand--back .brand__word { font-size: 40px; }
  .brand--back .brand__sub { font-size: 16.5px; margin-top: 7px; letter-spacing: 0.06em; }

  .services {
    position: absolute;
    left: 0; right: 0; top: 298px;
    text-align: center;
    font-size: 27px;
    line-height: 34px;
  }

  .doctor { position: absolute; left: 31px; top: 205px; }
  .doctor__name { font-size: 34px; line-height: 44px; }
  .doctor__letters { font-size: 20px; color: var(--accent); margin-left: 6px; }
  .doctor__diploma { font-size: 24px; color: var(--accent); line-height: 32px; }

  .divider {
    position: absolute;
    left: 31px; right: 31px; top: 306px;
    height: 2px;
    background: var(--accent);
  }

  .contact { position: absolute; left: 31px; top: 355px; list-style: none; }
  .contact li {
    display: flex; align-items: center;
    font-size: 28px; line-height: 33px;
  }
  .contact svg { width: 22px; height: 22px; margin-right: 16px; fill: var(--accent); }

  .social { position: absolute; right: 70px; top: 348px; display: flex; gap: 14px; }
  .social span {
    width: 31px; height: 31px; border-radius: 50%;
    background: var(--accent);
    display: flex; align-items: center; justify-content: center;
  }
  .website {
    position: absolute; right: 31px; top: 413px;
    font-size: 26px;
  }
</style>
</head>
<body>

<section class="card card--front">
  <div class="front-frame"></div>
  <div class="brand brand--front">
    <div class="brand__circle"></div>
    <div class="brand__name">
      <span class="brand__word">MORVELA</span>
      <span class="brand__sub">AESTHETIC DOCTOR</span>
    </div>
  </div>
  <p class="services">
    Dermal injectables - Plasma facials - Microneedling<br>
    Skin boosters - Excessive sweating<br>
    Home and Spa Based Treatments
  </p>
</section>

<section class="card card--back">
  <div class="brand brand--back">
    <div class="brand__circle"></div>
    <div class="brand__name">
      <span class="brand__word">MORVELA</span>
      <span class="brand__sub">AESTHETIC DOCTOR</span>
    </div>
  </div>

  <div class="doctor">
    <p class="doctor__name">Dr Lena Vorst<span class="doctor__letters">MRCPCH MD</span></p>
    <p class="doctor__diploma">Australasian Diploma of Aesthetic Medicine</p>
  </div>

  <div class="divider"></div>

  <ul class="contact">
    <li>
      <svg viewBox="0 0 24 24" aria-hidden="true"><path d="M6.6 10.8a15.1 15.1 0 0 0 6.6 6.6l2.2-2.2a1 1 0 0 1 1-.25 11.4 11.4 0 0 0 3.6.57 1 1 0 0 1 1 1V20a1 1 0 0 1-1 1A17 17 0 0 1 3 4a1 1 0 0 1 1-1h3.5a1 1 0 0 1 1 1c0 1.25.2 2.45.57 3.57a1 1 0 0 1-.25 1z"/></svg>
      0800 555 014
    </li>
    <li>
      <svg viewBox="0 0 24 24" aria-hidden="true"><path d="M2 5h20v14H2z M3.5 6.5 12 13l8.5-6.5" fill="none" stroke="#00aeef" stroke-width="2"/></svg>
      lena@morvela.co.nz
    </li>
  </ul>

  <div class="social" aria-label="Online links">
    <span>
      <svg width="19" height="19" viewBox="0 0 20 20" aria-hidden="true" fill="none" stroke="#fff" stroke-width="1.4">
        <circle cx="10" cy="10" r="8"/><ellipse cx="10" cy="10" rx="3.5" ry="8"/><path d="M2 10h16M3.5 5.5h13M3.5 14.5h13"/>
      </svg>
    </span>
    <span></span>
    <span></span>
  </div>
  <p class="website">www.morvela.co.nz</p>
</section>

</body>
</html>
```